50 Page Catalog Full Redesign New Look

We are looking for a redesign of our Catalog,

We are looking for a modern redesign of our Catalog, with our new logo most of the products will be the same with some new products as well.
Please use colors in the new logo attached
Attached is our current design please see this for what product will go in the catulog
Updates

Designs look the same

Target Market(s)

Automotive

Font styles to use
Other font styles liked:
• Our Font is outfit

Colors

Designer to choose colors to be used in the design.

```html
<!DOCTYPE html>
<html lang="en">
<head>
<meta charset="utf-8">
<title>Automotive Products &amp; Ideas 2021 — Korvane Promotional</title>
<link rel="stylesheet" href="https://fonts.googleapis.com/css2?family=Outfit:wght@200;600;800&display=swap">
<style>
  :root {
    --brand-blue: #0062a0;
    --frame-blue: #005d9c;
    --deep-navy: #00426e;
    --sky-blue: #1a8ccc;
    --mid-blue: #1573aa;
    --charcoal: #3a3735;
    --slate: #312d3b;
    --gold: #e1b007;
    --white: #ffffff;
    --black: #000000;
  }
  html, body {
    margin: 0;
    padding: 0;
    width: 975px;
    height: 1200px;
    overflow: hidden;
    background: var(--white);
  }
  .catalog-cover {
    display: block;
    width: 975px;
    height: 1200px;
    font-family: "Outfit", sans-serif;
  }
  .cover-title {
    fill: var(--white);
    font-weight: 200;
    font-size: 54px;
    letter-spacing: -0.5px;
  }
  .cover-year {
    fill: var(--brand-blue);
    font-weight: 800;
    font-size: 124px;
    letter-spacing: -8px;
  }
  .brand-name {
    fill: var(--brand-blue);
    font-weight: 600;
    letter-spacing: 1px;
  }
  .brand-name--main { font-size: 60px; }
  .brand-name--sub { font-size: 30px; letter-spacing: 2px; }
</style>
</head>
<body>
<svg class="catalog-cover" viewBox="0 0 975 1200" xmlns="http://www.w3.org/2000/svg">
  <defs>
    <linearGradient id="dashboard-tones" x1="0" y1="0" x2="1" y2="1">
      <stop offset="0" stop-color="#4d6678"/>
      <stop offset="0.45" stop-color="#1c2b52"/>
      <stop offset="1" stop-color="#2a2d35"/>
    </linearGradient>
    <linearGradient id="car-tones" x1="0" y1="0" x2="1" y2="1">
      <stop offset="0" stop-color="#c4222b"/>
      <stop offset="0.6" stop-color="#a81c24"/>
      <stop offset="1" stop-color="#6e1418"/>
    </linearGradient>
  </defs>

  <rect class="header-band" x="0" y="0" width="975" height="549" fill="var(--brand-blue)"/>

  <path class="quadrant-frame" d="M531 549 L87 549 A444 444 0 0 1 531 105 Z" fill="var(--charcoal)"/>
  <path class="quadrant-photo" role="img" aria-label="Photo of a car dashboard with steering wheel and illuminated instrument cluster"
        d="M512 531 L105 531 A407 407 0 0 1 512 124 Z" fill="url(#dashboard-tones)"/>

  <path class="quadrant-navy" d="M531 549 L531 177 A372 372 0 0 1 903 549 Z" fill="var(--deep-navy)"/>
  <path class="quadrant-sky" d="M549 531 L549 204 A327 327 0 0 1 876 531 Z" fill="var(--sky-blue)"/>
  <path class="quadrant-mid" d="M549 531 L549 352 A179 179 0 0 1 728 531 Z" fill="var(--mid-blue)"/>

  <path class="quadrant-slate" d="M512 568 L512 1078 A510 510 0 0 1 2 568 Z" fill="var(--slate)"/>
  <path class="quadrant-black" d="M512 568 L512 748 A180 180 0 0 1 332 568 Z" fill="var(--black)"/>

  <path class="quadrant-frame-blue" d="M531 568 L531 976 A427 427 0 0 0 957 568 Z" fill="var(--frame-blue)"/>
  <path class="quadrant-photo" role="img" aria-label="Photo of the front headlights of a red SUV"
        d="M549 568 L549 957 A389 389 0 0 0 938 568 Z" fill="url(#car-tones)"/>

  <rect class="gutter" x="0" y="549" width="975" height="19" fill="var(--white)"/>
  <rect class="gutter" x="512" y="531" width="19" height="37" fill="var(--white)"/>

  <circle class="hub-outer" cx="531" cy="549" r="124" fill="var(--white)"/>
  <circle class="hub-ring" cx="531" cy="549" r="106" fill="var(--gold)"/>
  <circle class="hub-inner" cx="531" cy="549" r="60" fill="var(--white)"/>

  <text class="cover-title" x="937" y="103" text-anchor="end">Automotive</text>
  <text class="cover-title" x="947" y="148" text-anchor="end">Products &amp; Ideas</text>

  <text class="cover-year" x="64" y="1172" textLength="254" lengthAdjust="spacingAndGlyphs">2021</text>

  <text class="brand-name brand-name--main" x="920" y="1128" text-anchor="end">KORVANE</text>
  <text class="brand-name brand-name--sub" x="920" y="1172" text-anchor="end">PROMOTIONAL</text>
</svg>
</body>
</html>
```